KETTLEFORGE Outdoor Group Fitness 'Move Up Wendarra'

We are an outdoor group fitness company and about to launch a new program. We operate in the Macarthur area and for our next program we want to put the challenge out to the entire community of Macrathur to get fit!We have been using the same ad for the last few months and I would like a new exciting design to get everyone talking about us and hope to get a heap of new clients to sign up as well!We cater for all fitness levels, men & women. We want the ad to appeal to those that want to lose weight and also to those that are already fit and want to take their fitness to the next level. We have a great team of trainers and our client base are a great group who all work together to achieve their health & fitness goals. I want the flyer to be able to be emailed out to our database, printed for letter box drops and put on Facebook.I have attached a copy of our previous flyers so you can see what we have used previously You can also see our website (although a bit outdated)Or our public facebook page at https://www.sociallink-example.net/pages/Kettleforge-Outdoor-Group-Fitness-Personal-Training/582104736291045 where you can have access to lots of photosSome photos that can be used are below or feel free to take some from our facebook page

Target Market(s)

Male & FemaleOverweight clients who want to lose weight but also fit clients who want to take their fitness to the next level or the extreme

Industry/Entity Type

Fitness

Font styles to use
Sans Serif

Requirements
Must have
• KETTLEFORGE Logo and the words Outdoor Group FitnessStick with out black & green corporate colorsPhotosThe words 'Move Up Wendarra'contact details such as phone number, email and web address and find us on facebook
Nice to have
• Can use similar wording to the previous flyer just after a new lookTo include some of the success stories if space allows (not sure if you can do a 2 page flyer - front and back)

```html
<!DOCTYPE html>
<html lang="en">
<head>
<meta charset="utf-8">
<title>KETTLEFORGE Outdoor Group Fitness – Kick Start Program</title>
<link rel="stylesheet" href="https://fonts.googleapis.com/css2?family=Open+Sans:wght@800&family=Roboto+Condensed:wght@300;400;700&display=swap">
<style>
  :root {
    --green: #00a650;
    --green-dark: #078a43;
    --green-light: #8dc63f;
    --orange: #f7941d;
    --red: #e8262a;
    --black: #000000;
    --white: #ffffff;
  }
  * { margin: 0; padding: 0; box-sizing: border-box; }
  html, body { width: 849px; height: 1200px; overflow: hidden; background: var(--white); }
  .flyer {
    position: relative;
    width: 849px;
    height: 1200px;
    overflow: hidden;
    background: var(--green);
    font-family: "Roboto Condensed", "Arial Narrow", sans-serif;
    color: var(--white);
  }
  .abs { position: absolute; }

  /* Header tabs */
  .tab {
    position: absolute;
    left: 0;
    background: var(--green-dark);
    border-radius: 0 30px 30px 0;
    box-shadow: 3px 4px 6px rgba(0,0,0,.28);
    font-family: "Open Sans", sans-serif;
    font-weight: 800;
    font-size: 21px;
    padding-left: 29px;
    display: flex;
    align-items: center;
  }
  .tab--tagline { top: 109px; width: 347px; height: 50px; }
  .tab--region { top: 171px; width: 294px; height: 56px; }

  .intro { left: 385px; top: 100px; width: 440px; }
  .intro__kicker { font-weight: 300; font-size: 35px; line-height: 1; letter-spacing: -0.2px; }
  .intro__headline { margin-top: 12px; font-weight: 700; font-size: 47px; line-height: 50px; letter-spacing: -0.3px; }

  /* Meter band */
  .meter { left: 0; top: 290px; width: 849px; height: 110px; }
  .meter__label, .meter__goal {
    position: absolute; top: 324px;
    font-weight: 700; font-size: 44px; line-height: 1;
  }
  .meter__label { left: 70px; }
  .meter__goal { left: 584px; }

  /* Photo area */
  .photo { top: 399px; height: 600px; }
  .photo--action { left: 0; width: 380px; background: linear-gradient(170deg, #6f8a62 0%, #5d7d45 35%, #4f8a3a 60%, #2c3a2a 100%); }
  .photo--group { left: 380px; width: 469px; background: linear-gradient(175deg, #1d8a46 0%, #13a04e 45%, #0d9a48 100%); }

  .waves { left: 0; top: 820px; width: 849px; height: 380px; }

  /* Program */
  .program { left: 383px; top: 418px; width: 450px; }
  .program__title { font-weight: 700; font-size: 50px; line-height: 49px; letter-spacing: -0.3px; }
  .program__subtitle { margin-top: 17px; font-weight: 700; font-size: 29px; line-height: 1; }
  .program__list { list-style: none; margin-top: 10px; font-weight: 400; font-size: 25px; line-height: 34px; }

  /* Footer */
  .brand {
    left: 31px; top: 1078px;
    display: flex; align-items: center; gap: 10px;
    font-family: "Open Sans", sans-serif;
    font-weight: 800; font-size: 36px; color: var(--green);
    letter-spacing: 0.5px;
  }
  .brand__dot { width: 16px; height: 16px; border-radius: 50%; background: var(--green); }

  .contact { left: 330px; top: 1047px; width: 272px; text-align: right; }
  .contact__phone { font-weight: 700; font-size: 34px; letter-spacing: 3px; line-height: 38px; }
  .contact__line { font-weight: 400; font-size: 24px; line-height: 34px; }
  .divider { left: 620px; top: 1044px; width: 2px; height: 114px; background: var(--white); }
  .cta { left: 637px; top: 1085px; font-weight: 700; font-size: 29px; line-height: 1; }
</style>
</head>
<body>
<main class="flyer">
  <div class="tab tab--tagline">Outdoor Group Fitness</div>
  <div class="tab tab--region">Move Up Wendarra</div>

  <div class="abs intro">
    <p class="intro__kicker">Change your health &amp; fitness</p>
    <h1 class="intro__headline">Experience a workout<br>like no other!</h1>
  </div>

  <svg class="abs meter" viewBox="0 0 849 110" aria-hidden="true">
    <defs>
      <linearGradient id="meterGradient" x1="0" x2="1" y1="0" y2="0">
        <stop offset="0" stop-color="#e8262a"/>
        <stop offset="0.55" stop-color="#f7941d"/>
        <stop offset="0.8" stop-color="#8dc63f"/>
        <stop offset="1" stop-color="#00a650"/>
      </linearGradient>
    </defs>
    <path d="M0 30 Q220 4 849 8 L849 110 L0 110 Z" fill="url(#meterGradient)"/>
    <g fill="#ffffff">
      <polygon points="378,48 391,48 401,57 391,66 378,66 388,57"/>
      <polygon points="398,42 415,42 428,57 415,72 398,72 411,57"/>
      <polygon points="423,35 444,35 461,57 444,79 423,79 440,57"/>
      <polygon points="455,27 482,27 503,57 482,87 455,87 476,57"/>
      <polygon points="494,18 528,18 553,57 528,96 494,96 519,57"/>
    </g>
  </svg>
  <div class="meter__label">FITNESS METER</div>
  <div class="meter__goal">OUR GOAL</div>

  <div class="abs photo photo--action" role="img" aria-label="Photo of trainers working out outdoors: a plate press and tyre jumps on the grass"></div>
  <div class="abs photo photo--group" role="img" aria-label="Green-tinted photo of a group class exercising with medicine balls on a sports field"></div>

  <svg class="abs waves" viewBox="0 0 849 380" aria-hidden="true">
    <path d="M0 140 Q450 165 849 30 L849 380 L0 380 Z" fill="#00a650"/>
    <path d="M0 183 Q480 168 849 58 L849 380 L0 380 Z" fill="#000000"/>
  </svg>

  <section class="abs program">
    <h2 class="program__title">New 4-Week<br>Kick Start 2014<br>Program</h2>
    <h3 class="program__subtitle">Our Sessions include:</h3>
    <ul class="program__list">
      <li>Boxing &amp; Kickboxing for fitness</li>
      <li>Core Strength</li>
      <li>Tabata Training</li>
      <li>Circuit &amp; Strength Trainging</li>
      <li>Bootcamp</li>
      <li>Bench Training &amp; Hardcore Sessions</li>
      <li>Fitness Challenges + more</li>
    </ul>
  </section>

  <div class="abs brand"><span class="brand__dot"></span>KETTLEFORGE</div>

  <div class="abs contact">
    <p class="contact__phone">0412555038</p>
    <p class="contact__line">info@kettleforge.com.au</p>
    <p class="contact__line">www.kettleforge.com.au</p>
  </div>
  <div class="abs divider"></div>
  <p class="abs cta">Join Us today</p>
</main>
</body>
</html>
```